Vantry Forge (IT/Network Services)

Vantry Forge, LLC provides technology services to small and medium businesses. Essentially, anytime you've every thought your business might need an "IT guy" to handle something you could instead call us to handle it. Basically, you can outsource your IT needs to us.

This is a brand new company and so we'll need a brand new website. I'd like to use WordPress to handle the site since that will make things easier for me to maintain in the long run.

The site should include a, more-or-less, static front page with the dynamic data occurring on pages linked from a navigational area.

I have a logo already designed that I would like to see used in the design. The one with "white" in the title is the official logo, just added some other versions for your perusal.

Color queues from the logo but feel free to add other colors where applicable.

The site should feel somewhat corporate but with a "younger" slant (something a 25-35 year old would enjoy).

Pages (either to be added initially or by me after design completion):
"About" section - includes company history, business philosophy, etc.
"Services" section - service options, service approach, service specifics
"Testimonials" section - (eventually)
"News" section - (eventually) industry news, company news, events, blog
Contact Links

Websites to view:
The two largest local competitors:
http://www.harbelmsystemsinc.example/
http://www.qubrix.example/
Other local competitors:
http://www.plkllc.example/
http://www.merowaygroup.example/

Other info you might find useful:
Domain: vfllc.example
Address:
517 Calder Ln W
Suite 742B
Nashville, TN 37288
Phone: 615-555-0187
Emails available for use/display:
info@vfllc.example
sales@vfllc.example

Target Market(s)

Our target clients are mainly small businesses (25 or less computer users) which means we're looking at a lot of start-ups or younger companies. We'll be interacting with many entrepreneurs and young business owners.

Requirements
Must have
• Need full WP theme (not a mockup)

```html
<!DOCTYPE html>
<html lang="en">
<head>
<meta charset="utf-8">
<title>Vantry Forge — IT &amp; Network Services</title>
<link rel="stylesheet" href="https://fonts.googleapis.com/css2?family=Roboto+Condensed:ital,wght@0,300;0,400;0,700;1,400&family=Arimo:wght@400;700&display=swap">
<style>
:root{
  --orange:#f7941d;
  --slate:#6d7179;
  --page:#ebebeb;
  --white:#ffffff;
  --text:#4a4a4a;
  --muted:#8a8a8a;
  --cond:"Roboto Condensed", Arial, sans-serif;
  --body:"Arimo", Arial, sans-serif;
}
*{box-sizing:border-box;margin:0;padding:0}
html,body{width:1200px;height:1151px;overflow:hidden;background:var(--page)}
.site{position:relative;width:980px;height:940px;transform:scale(1.2245);transform-origin:0 0;font-family:var(--body);color:var(--text)}
.topbar{position:absolute;left:0;top:0;width:980px;height:84px;background:var(--white)}
.brand{position:absolute;left:0;top:0;width:200px;height:130px;background:var(--white);display:flex;align-items:center;justify-content:center;gap:8px}
.brand-dot{width:14px;height:14px;border-radius:50%;background:var(--orange)}
.brand-name{font-family:var(--cond);font-weight:700;font-size:24px;color:var(--slate);white-space:nowrap}
.phone{position:absolute;right:0;top:8px;display:flex;align-items:center;gap:6px;font-family:var(--cond);font-size:18px;color:var(--orange);white-space:nowrap}
.nav{position:absolute;top:48px;left:546px;display:flex;gap:3px}
.nav a{display:block;height:36px;line-height:36px;text-align:center;white-space:nowrap;background:var(--slate);color:var(--white);font-family:var(--cond);font-size:17px;text-decoration:none}
.nav a.active{background:var(--orange);position:relative}
.nav a.active::after{content:"";position:absolute;left:50%;bottom:-1px;margin-left:-5px;border:5px solid transparent;border-bottom-color:var(--page)}
.quote{position:absolute;left:0;top:145px;width:200px;height:263px;background:linear-gradient(90deg,#6e737b,#8b8f96 55%,#6e737b);border-radius:0 3px 3px 0;padding:18px 10px 0 15px;font-family:var(--cond);font-style:italic;font-size:14.5px;line-height:26px;color:var(--white)}
.quote .mark{color:var(--orange);font-weight:700;font-size:20px}
.quote-tail{position:absolute;left:0;top:408px}
.quote-author{position:absolute;left:48px;top:413px;font-family:var(--cond);font-weight:700;font-size:20px;color:var(--slate);white-space:nowrap}
.hero{position:absolute;left:216px;top:98px;width:764px;height:320px;border-radius:4px 0 0 4px;background:linear-gradient(180deg,#f4f4f4 0%,#e3dfdb 55%,#cfd2d6 100%);overflow:hidden}
.hero-caption{position:absolute;left:4px;top:249px;width:415px;height:66px;background:rgba(40,40,40,.6);color:var(--white);font-family:Arial, sans-serif;font-size:26px;line-height:66px;padding-left:18px;white-space:nowrap}
.hero-caption b{font-size:38px;font-weight:700}
.dots{position:absolute;left:578px;top:426px;display:flex;gap:5px}
.dots span{width:10px;height:10px;border-radius:50%;background:var(--slate)}
.dots span.on{background:var(--orange)}
.welcome{position:absolute;left:0;top:450px;width:700px}
.welcome h1{font-family:var(--cond);font-weight:300;font-size:25px;color:var(--orange);padding-bottom:6px;border-bottom:1px dashed #bdbdbd;white-space:nowrap}
.welcome p{margin-top:9px;font-size:11px;line-height:18px;color:var(--muted);text-align:justify}
.card{position:absolute;top:602px;width:340px;height:273px;background:var(--white);border-radius:4px;padding:12px 14px}
.card h2,.news-item h3{font-family:var(--body);font-weight:700;color:var(--orange);white-space:nowrap}
.card h2{font-size:16px}
.card .photo{margin-top:8px;width:311px;height:142px;border-radius:4px;background:linear-gradient(90deg,#d9b8a1,#c7a896 40%,#ada39d 70%,#8d8884)}
.card p{margin-top:8px;font-size:11px;line-height:18px}
.more{display:inline-block;margin-top:2px;font-size:11px;font-weight:700;color:#111;text-decoration:none}
.more::after{content:" \203A";color:var(--orange)}
.news-head{position:absolute;left:722px;top:450px;display:flex;align-items:center;gap:10px;font-family:var(--cond);font-size:25px;color:var(--orange);white-space:nowrap}
.news{position:absolute;left:720px;top:490px;width:258px;height:318px;border:2px solid #cdcdcd;background:#f3f3f3}
.news-item{padding:10px 14px 8px;border-bottom:1px solid #d6d6d6}
.news-item:last-child{border-bottom:0}
.news-item h3{font-size:12px}
.news-item p{margin-top:4px;font-size:10.5px;line-height:16px}
.footer{position:absolute;left:0;top:895px;width:980px;height:45px;background:var(--slate);color:var(--white);font-size:11px;line-height:45px;white-space:nowrap}
.social{position:absolute;right:2px;top:8px;display:flex;gap:8px}
.social span{width:29px;height:29px;border-radius:50%;background:var(--white);border:2px solid #d8d8d8}
</style>
</head>
<body>
<div class="site">
  <header class="topbar"></header>
  <div class="brand"><span class="brand-dot"></span><span class="brand-name">Vantry Forge</span></div>
  <div class="phone">
    <svg width="22" height="14" viewBox="0 0 22 14" aria-hidden="true"><path d="M1 5c0-3 20-3 20 0v2h-5V4H6v3H1z M5 8h12l2 6H3z" fill="#6d7179"/></svg>
    615-555-0187
  </div>
  <nav class="nav">
    <a class="active" href="#" style="width:66px">Home</a><a href="#" style="width:88px">About Us</a><a href="#" style="width:83px">Services</a><a href="#" style="width:88px">Solutions</a><a href="#" style="width:98px">Contact Us</a>
  </nav>

  <blockquote class="quote"><span class="mark">&ldquo;</span> Lorem Ipsum is simply dummy text of the printing and typesetting industry. Lorem Ipsum has been the industry's standard dummy text ever since the 1500s, when an unknown printer took a galley of type and scrambled it to make a type specimen book.<span class="mark"> &rdquo;</span></blockquote>
  <svg class="quote-tail" width="40" height="28" viewBox="0 0 40 28" aria-hidden="true"><path d="M0 0H40L40 28Z" fill="#6e737b"/></svg>
  <div class="quote-author">Dale Corbin</div>

  <section class="hero" role="img" aria-label="Photo of a smiling business team of five in office attire">
    <div class="hero-caption"><b>WITH US!</b> Be Successful</div>
  </section>
  <div class="dots"><span class="on"></span><span></span><span></span></div>

  <section class="welcome">
    <h1>Welcome to Vantry Forge</h1>
    <p>Lorem Ipsum is simply dummy text of the printing and typesetting industry. Lorem Ipsum has been the industry's standard dummy text ever since the 1500s, when an unknown printer took a galley of type and scrambled it to make a type specimen book. It has survived not only five centuries, but also the leap into electronic typesetting, remaining essentially unchanged. It was popularised in the 1960s with the release of Pressmark sheets containing Lorem Ipsum passages, and more recently with desktop publishing software like Quillset Layout including versions of Lorem Ipsum.</p>
  </section>

  <article class="card" style="left:0">
    <h2>Lorem Ipsum is simply</h2>
    <div class="photo" role="img" aria-label="Photo of a support agent wearing a headset with colleagues behind"></div>
    <p>Lorem Ipsum is simply dummy text of the printing and typesetting industry. Lorem Ipsum has been the industry's standard dummy text ever since the 1500s,</p>
    <a class="more" href="#">Read More</a>
  </article>
  <article class="card" style="left:360px">
    <h2>Lorem Ipsum is simply</h2>
    <div class="photo" role="img" aria-label="Photo of a support agent wearing a headset with colleagues behind"></div>
    <p>Lorem Ipsum is simply dummy text of the printing and typesetting industry. Lorem Ipsum has been the industry's standard dummy text ever since the 1500s,</p>
    <a class="more" href="#">Read More</a>
  </article>

  <div class="news-head">
    <svg width="42" height="26" viewBox="0 0 42 26" aria-hidden="true"><rect x="1" y="1" width="40" height="24" rx="2" fill="#fff" stroke="#6d7179" stroke-width="2"/><rect x="5" y="5" width="18" height="6" fill="#6d7179"/><path d="M5 15h32M5 19h32M26 6h11M26 10h11" stroke="#6d7179" stroke-width="1.5"/></svg>
    Letset News
  </div>
  <aside class="news">
    <div class="news-item"><h3>Lorem Ipsum is simply</h3><p>Lorem Ipsum is simply dummy text of the print-been the industry's standard dummy text ever since the 1500s,</p><a class="more" href="#">Read more</a></div>
    <div class="news-item"><h3>Lorem Ipsum is simply</h3><p>Lorem Ipsum is simply dummy text of the print-since the 1500s,</p><a class="more" href="#">Read more</a></div>
    <div class="news-item"><h3>Lorem Ipsum is simply</h3><p>Lorem Ipsum is simply dummy text of the print been the industry's standard dummy text ever since the 1500s, been the industry's standard dummy text..</p><a class="more" href="#">Read more</a></div>
  </aside>

  <footer class="footer">Copyright @ 2012 Vantry Forge, All Rights Reserved
    <div class="social"><span></span><span></span><span></span></div>
  </footer>
</div>
</body>
</html>
```